Gutschein-Design für Bauträgerfirma
Sehr guter Designer, würde ich immer wieder weiter empfehlen.
Zielgruppe
Wir sind eine Bauträgerfirma und verkaufen Wohnungen für die gehobene Klasse.
Aufgabenstellung
Auflösung min. 150dpi, Format: 3,56m x 2,52m,
Dieses Banner soll eine Werbung bzw. einen Gutschein enthalten.
Folgender Text soll enthalten sein: Wenn Sie eine Wohnung bis zum 31.12.2018 bei uns kaufen, erhalten Sie einen Bemusterungsgutschein von 5.000€.
Der Text kann natürlich auch anders formuliert werden, der Kern sollte erhalten bleiben.
Die Unterlagen können auch im anderen Format zur Verfügung gestellt werden. Es sind alle Render in großem Format verfügbar.

```html
<!DOCTYPE html>
<html lang="de">
<head>
<meta charset="utf-8">
<title>Halder Immobilien – Bemusterungsgutschein</title>
<link rel="stylesheet" href="https://fonts.googleapis.com/css2?family=Open+Sans:wght@300;400&display=swap">
<style>
  :root {
    --navy: #0f2a4a;
    --navy-text: #2c3a63;
    --frame: #3a4a70;
    --white: #ffffff;
    --bullet-text: #e9edf4;
  }
  * { margin: 0; padding: 0; box-sizing: border-box; }
  html, body {
    width: 1200px; height: 910px; overflow: hidden;
    background: var(--white);
    font-family: "Open Sans", Arial, sans-serif;
  }
  .banner {
    position: absolute; left: 153px; top: 119px;
    width: 890px; height: 630px;
    border: 1px solid var(--frame);
    background: var(--white);
    overflow: hidden;
  }
  .hero {
    position: absolute; left: 0; top: 0; width: 100%; height: 686px;
    background: var(--navy);
  }
  .hero-photo {
    position: absolute; left: 0; top: 0; width: 100%; height: 420px;
    background: linear-gradient(180deg,
      #f3efe9 0%, #e8e1d7 14%, #c9c5b5 28%, #aeaf98 38%,
      #a5999a 52%, #8a8793 64%, #4f5b75 80%, var(--navy) 100%);
  }
  .headline-box {
    position: absolute; left: 0; width: 791px;
    background: var(--white);
    border: 2px solid #6c7590; border-left: none;
    color: var(--navy-text);
    font-weight: 300; font-size: 28px; line-height: 38px;
    padding-left: 46px;
  }
  .headline-question { top: 149px; height: 51px; padding-top: 6px; }
  .headline-offer { top: 231px; height: 99px; padding-top: 11px; }
  .brand {
    position: absolute; left: 56px; top: 400px; width: 300px;
    display: flex; flex-direction: column; align-items: center;
  }
  .brand-mark { width: 26px; height: 26px; background: var(--white); margin-bottom: 22px; }
  .brand-name {
    color: var(--white); font-weight: 400; font-size: 34px;
    letter-spacing: 0.5px; white-space: nowrap;
  }
  .features {
    position: absolute; left: 484px; top: 411px;
    list-style: none; color: var(--bullet-text);
    font-weight: 300; font-size: 19px; line-height: 24.6px;
  }
  .features li::before { content: "\2022"; font-size: 13px; margin-right: 7px; vertical-align: 2px; }
  .contact {
    position: absolute; left: 0; top: 567px; width: 100%; height: 63px;
    background: var(--white);
    color: var(--navy-text); font-size: 19px; font-weight: 400;
    display: flex; align-items: center; justify-content: center;
  }
</style>
</head>
<body>
  <section class="banner">
    <div class="hero">
      <div class="hero-photo" role="img" aria-label="Luftaufnahme einer Stadt mit Feldern und Hügeln im Dunst"></div>
    </div>

    <p class="headline-box headline-question">SIE KAUFEN EINE WOHNUNG BIS ZUM 31.12.2018?</p>
    <p class="headline-box headline-offer">DANN ERHALTEN SIE EINEN<br>BEMUSTERUNGSGUTSCHEIN IM WERT VON 5.000€!</p>

    <div class="brand">
      <span class="brand-mark"></span>
      <span class="brand-name">HALDER IMMOBILIEN</span>
    </div>

    <ul class="features">
      <li>HOCHMODERNE ARCHITEKTUR</li>
      <li>TOP-LAGEN</li>
      <li>HOCHWERTIGE AUSSTATTUNG</li>
      <li>FAIRES PREIS-LEISTUNGSVERHÄLTNIS</li>
      <li>ÜBERZEUGENDE QUALITÄT</li>
    </ul>

    <footer class="contact">TELEFON: 07000/318 52 64 &nbsp;•&nbsp; HALDER-IMMOBILIEN.COM</footer>
  </section>
</body>
</html>
```